Dear All,

We need a book cover for our interactive eTome on Varlen to be released on the Quince ShelfHub.

The book consists of 10 curated chapters that include, music, audio interviews, images, short films and panel discussions.

Here is the trailer for the book:

https://clipvault.example/48213577

Throughout the project we have attempted to build something that uses lots of types of media content but at its core reads like a traditional book. Ideally we want a cover that reflects this. I.e something that looks to the future but doesn't forget the past. Most eTomes released on Varlen generally use the famous portrait of Varlen wearing a red coat. See below: We would like to avoid this.

https://www.findwell.example/search?q=brahms+green+cloak

The brief is relatively open as we are after wide range of applicants. The only thing that is a must is the words and the font that we have used throughout the book.

Words on cover:

The Varlen Venture

By The Lanternfold Guild

The font that we have been using for the titles of the book is Langdon. I will include
the font in the upload section.

Tech specs:

Size: 768 x 1004 pixels.
Type: JPEG

Please contact me with any questions.

Many Thanks,

tobin@lanternfoldworks.example

Requirements
Must have
• Words:

They Brahms Venture
by The Lanternfold Guild
Nice to have
• Something that is elegant, abstract but recognizable

The color blue and ample white background space
Should not have
• should not use a traditional Varlen portrait. However it could draw inspiration from or be a remix of a traditional image of Varlen.

```html
<!DOCTYPE html>
<html lang="en">
<head>
<meta charset="utf-8">
<title>The Varlen Venture — Cover</title>
<link rel="stylesheet" href="https://fonts.googleapis.com/css2?family=Bebas+Neue&family=Mulish:wght@400&display=swap">
<style>
  :root {
    --slate: #505e6b;
    --slate-soft: #6f7f8c;
    --credit-grey: #939ea8;
    --paper: #ffffff;
    --teal: #62c0c4;
    --mauve: #876985;
    --mustard: #ddb83f;
    --indigo: #414a7d;
    --mist: #e0dedb;
    --crimson: #a31c32;
    --tangerine: #e0742a;
    --sand: #b7a891;
    --leaf: #8dbb5a;
    --portrait-light: #b9a58a;
    --portrait-dark: #2a211a;
  }
  * { margin: 0; padding: 0; box-sizing: border-box; }
  html, body { width: 1200px; height: 918px; overflow: hidden; background: var(--paper); }
  .cover { position: relative; width: 1200px; height: 918px; background: var(--paper); }

  .title-line {
    position: absolute;
    left: 28px;
    font-family: "Bebas Neue", "Oswald", sans-serif;
    font-weight: 400;
    font-size: 229px;
    line-height: 1;
    letter-spacing: 7px;
    color: var(--slate);
    white-space: nowrap;
  }
  .title-line--first { top: 7px; }
  .title-line--second { top: 235px; }

  .tagline {
    position: absolute;
    left: 733px;
    top: 250px;
    font-family: "Mulish", "Muli", sans-serif;
    font-size: 36px;
    line-height: 45px;
    letter-spacing: 0.6px;
    color: var(--slate-soft);
  }

  .chapter-dots { position: absolute; left: 0; top: 0; }

  .credit-bar {
    position: absolute;
    left: 0; bottom: 0;
    width: 1200px; height: 56px;
    background: var(--slate);
    display: flex;
    align-items: center;
  }
  .credit-bar__author {
    margin-left: 22px;
    font-family: "Bebas Neue", "Oswald", sans-serif;
    font-size: 44px;
    letter-spacing: 1.5px;
    color: var(--paper);
    line-height: 1;
    padding-top: 4px;
  }
  .credit-bar__director {
    margin-left: 46px;
    font-family: "Mulish", "Muli", sans-serif;
    font-size: 34px;
    letter-spacing: 1.5px;
    color: var(--credit-grey);
  }
</style>
</head>
<body>
<main class="cover">
  <h1>
    <span class="title-line title-line--first">The Varlen</span>
    <span class="title-line title-line--second">Venture</span>
  </h1>

  <p class="tagline">by the worlds<br>greatest scholars<br>critics and<br>performers</p>

  <svg class="chapter-dots" width="1200" height="918" viewBox="0 0 1200 918">
    <defs>
      <radialGradient id="portrait-tone" cx="50%" cy="40%" r="60%">
        <stop offset="0%" stop-color="var(--portrait-light)"/>
        <stop offset="100%" stop-color="var(--portrait-dark)"/>
      </radialGradient>
    </defs>
    <circle cx="120" cy="548" r="80" fill="var(--teal)"/>
    <circle cx="355" cy="548" r="80" fill="var(--mauve)"/>
    <circle cx="592" cy="548" r="80" fill="var(--mustard)"/>
    <circle cx="827" cy="548" r="80" fill="var(--indigo)"/>
    <circle cx="1062" cy="548" r="80" fill="var(--mist)"/>
    <circle cx="120" cy="752" r="80" fill="var(--crimson)"/>
    <circle cx="355" cy="752" r="80" fill="var(--tangerine)"/>
    <circle cx="592" cy="752" r="80" fill="var(--sand)"/>
    <circle cx="827" cy="752" r="80" fill="var(--leaf)"/>
    <circle cx="1062" cy="752" r="80" fill="url(#portrait-tone)" role="img" aria-label="Round painted portrait of the young composer"/>
  </svg>

  <footer class="credit-bar">
    <span class="credit-bar__author">By The Lanternfold Guild</span>
    <span class="credit-bar__director">directed by sir julian marlowe</span>
  </footer>
</main>
</body>
</html>
```